Residential Remodeling Contractor needs updated business card

I need a new design for my business card.
Name of the company is Brookfell Construction. I need a card that commands presence, strength, integrity. I have been in business for 28 years. I am a Residential Remodeling Contractor that covers all aspects of a residential remodel and build.

```html
<!DOCTYPE html>
<html lang="en">
<head>
<meta charset="utf-8">
<title>Brookfell Construction — Business Card</title>
<link rel="stylesheet" href="https://fonts.googleapis.com/css2?family=Lora:wght@400;500&display=swap">
<style>
  :root {
    --page-bg: #d4d5d8;
    --card-deep: #1e3772;
    --card-light: #27478f;
    --ink: #ffffff;
    --ink-soft: #e6ebf7;
  }
  * { margin: 0; padding: 0; box-sizing: border-box; }
  html, body {
    width: 900px; height: 1200px; overflow: hidden;
    background: var(--page-bg);
    font-family: "Lora", Georgia, serif;
    color: var(--ink);
  }
  .canvas { position: relative; width: 900px; height: 1200px; }
  .card {
    position: absolute;
    width: 633px; height: 364px;
    background: linear-gradient(160deg, var(--card-deep) 0%, var(--card-light) 100%);
  }
  .card--front { left: 133px; top: 210px; }
  .card--back  { left: 134px; top: 624px;
    background: linear-gradient(200deg, var(--card-light) 0%, var(--card-deep) 100%); }

  .wordmark {
    position: absolute;
    font-weight: 500;
    font-variant: small-caps;
    line-height: 1.02;
    color: var(--ink);
    letter-spacing: 0.01em;
  }
  .card--front .wordmark {
    left: 0; right: 0; top: 150px;
    text-align: center;
    font-size: 44px;
  }
  .card--back .wordmark {
    left: 54px; top: 164px;
    font-size: 33px;
  }
  .divider {
    position: absolute;
    left: 316px; top: 94px;
    width: 1.5px; height: 177px;
    background: var(--ink);
  }
  .details { position: absolute; left: 333px; top: 112px; }
  .person-name {
    font-size: 24px; font-weight: 500;
    letter-spacing: 0.04em; text-transform: uppercase;
    line-height: 1.1;
  }
  .person-role {
    margin-top: 5px;
    font-size: 14px; color: var(--ink-soft);
    letter-spacing: 0.03em;
  }
  .contact-list { list-style: none; margin-top: 30px; }
  .contact-list li {
    display: flex; align-items: center; gap: 7px;
    font-size: 14px; letter-spacing: 0.05em;
    height: 23.5px;
  }
  .contact-list svg { width: 14px; height: 14px; flex: none; fill: var(--ink); }
</style>
</head>
<body>
<main class="canvas">
  <section class="card card--front" aria-label="Card front">
    <div class="wordmark">Brookfell<br>Construction</div>
  </section>

  <section class="card card--back" aria-label="Card back">
    <div class="wordmark">Brookfell<br>Construction</div>
    <div class="divider"></div>
    <div class="details">
      <h1 class="person-name">Mateo Ferrandis</h1>
      <p class="person-role">Residential Remodeling Contractor</p>
      <ul class="contact-list">
        <li>
          <svg viewBox="0 0 24 24" aria-hidden="true"><path d="M6.6 10.8a15.1 15.1 0 0 0 6.6 6.6l2.2-2.2c.3-.3.7-.4 1-.2 1.1.4 2.3.6 3.6.6.6 0 1 .4 1 1V20c0 .6-.4 1-1 1A17 17 0 0 1 3 4c0-.6.4-1 1-1h3.5c.6 0 1 .4 1 1 0 1.3.2 2.5.6 3.6.1.3 0 .7-.2 1z"/></svg>
          17785550192
        </li>
        <li>
          <svg viewBox="0 0 24 24" aria-hidden="true"><path d="M2 5h20v14H2z M3.5 6.5l8.5 6.5 8.5-6.5" fill="none" stroke="#fff" stroke-width="1.8"/><path d="M2 5h20l-10 7.5z"/></svg>
          info@brookfellconstruction.com
        </li>
        <li>
          <svg viewBox="0 0 24 24" aria-hidden="true"><g fill="none" stroke="#fff" stroke-width="1.6"><circle cx="12" cy="12" r="9.5"/><ellipse cx="12" cy="12" rx="4" ry="9.5"/><path d="M2.5 12h19M4 7h16M4 17h16"/></g></svg>
          brookfellconstruction.com
        </li>
      </ul>
    </div>
  </section>
</main>
</body>
</html>
```